KTW Structural Approval Partners Certifiers

Professional Construction Consultancy Company Business Card - must keep logo colours see images below - examples have been added from my last competition - please see them as examples only!

Target Market(s)

Home Builders

Industry/Entity Type

Construction

Contact Information for Business Card

See "must haves"

Font styles to use
Sans Serif

Colors
ffffff
add136
000000

Requirements
Must have
• Daniel Moravec
• Director
• Phone: 0431 758 219
• Address: 17 Corrigan St,
• Holloway Vale, SA, 5098
• Email: ktwapprovalpartners@mailbox-example.com
• Website: www.ktwapprovalpartners.example.au
• Facebook: KTW Structural Approval Partners
Nice to have
• Side 1: full logo
• Side 2: company details
Should not have
• hard to read
• must be clear and professional

```html
<!DOCTYPE html>
<html lang="en">
<head>
<meta charset="utf-8">
<title>KTW Structural Approval Partners Certifiers – Business Card</title>
<link rel="stylesheet" href="https://fonts.googleapis.com/css2?family=Montserrat:wght@600&family=Roboto:wght@700;900&display=swap">
<style>
  :root {
    --stage: #5b4a3a;
    --card: #1c1c1c;
    --green: #add136;
    --white: #ffffff;
    --black: #000000;
  }
  * { margin: 0; padding: 0; box-sizing: border-box; }
  html, body { width: 1200px; height: 987px; overflow: hidden; }
  body { background: var(--stage); position: relative; }

  .card {
    position: absolute;
    left: 293px;
    width: 615px;
    height: 350px;
    background: var(--card);
  }
  .card--details { top: 130px; }
  .card--brand { top: 505px; }

  .wordmark {
    position: absolute;
    left: 0; right: 0;
    text-align: center;
    font-family: "Montserrat", sans-serif;
    font-weight: 600;
    color: var(--green);
    text-transform: uppercase;
    line-height: 1.12;
  }
  .card--details .wordmark { top: 46px; font-size: 27px; letter-spacing: 1.5px; }
  .card--brand .wordmark { top: 100px; font-size: 33px; letter-spacing: 2px; }
  .wordmark .tagline { display: block; letter-spacing: 6px; }

  .person {
    position: absolute;
    left: 0;
    width: 243px;
    top: 208px;
    text-align: right;
    font-family: "Roboto", sans-serif;
    font-weight: 700;
    color: var(--white);
  }
  .person__name { font-size: 24px; font-weight: 900; line-height: 1.1; }
  .person__role { font-size: 16px; margin-top: 3px; }
  .person__address { font-size: 14px; line-height: 1.55; margin-top: 9px; }

  .contact {
    position: absolute;
    left: 275px;
    top: 211px;
    list-style: none;
    font-family: "Roboto", sans-serif;
    font-weight: 700;
    font-size: 13.5px;
    color: var(--white);
  }
  .contact li { display: flex; align-items: center; height: 23.5px; white-space: nowrap; }
  .contact svg { width: 14px; height: 14px; margin-right: 9px; flex: none; fill: var(--green); }
</style>
</head>
<body>

<section class="card card--details">
  <div class="wordmark">
    KTW Structural<br>Approval Partners
    <span class="tagline">Certifiers</span>
  </div>

  <div class="person">
    <div class="person__name">DANIEL MORAVEC</div>
    <div class="person__role">Director</div>
    <div class="person__address">17 Corrigan St<br>Holloway Vale, SA, 5098</div>
  </div>

  <ul class="contact">
    <li>
      <svg viewBox="0 0 16 16" aria-hidden="true"><path d="M2 6c0-2 2.5-3 6-3s6 1 6 3v1h-3V5.5H5V7H2z M4 8h8l1.5 5h-11z"/></svg>
      0431 758 219
    </li>
    <li>
      <svg viewBox="0 0 16 16" aria-hidden="true"><path d="M1 3h14v1.5L8 9 1 4.5z M1 6.3l7 4.5 7-4.5V13H1z"/></svg>
      ktwapprovalpartners@mailbox-example.com
    </li>
    <li>
      <svg viewBox="0 0 16 16" aria-hidden="true"><circle cx="8" cy="8" r="7"/><path d="M1 8h14M8 1c-3 3-3 11 0 14M8 1c3 3 3 11 0 14" stroke="#1c1c1c" stroke-width="1.2" fill="none"/></svg>
      www.ktwapprovalpartners.example.au
    </li>
    <li>
      <svg viewBox="0 0 16 16" aria-hidden="true"><rect x="1" y="1" width="14" height="14"/></svg>
      KTW Structural Approval Partners
    </li>
  </ul>
</section>

<section class="card card--brand">
  <div class="wordmark">
    KTW Structural<br>Approval Partners
    <span class="tagline">Certifiers</span>
  </div>
</section>

</body>
</html>
```